Clear Current Monthly Bulletin

I would like to have some backgrounds designed for July - December. We would pay for each page seperately. Each month should be its own design so that we may pick the best month for each. You are welcome to submit as many designs as you like for months. Months with themes will rate higher, for example July can incorporate Independence Day, December Christmas Season/Yule/Hannukah/Holidays,October Halloween, November Thanksgiving, September Labor Day, August can be summer themed. I am attaching our newsletter that I would like the design to work around. This verbiage does not need to be on the page right now. We would like to have the verbiage for each month applied to that month on purchase. www.tolvanwiring.com is our website. We love designs that stay with our colors and website theme.

Target Market(s)

Homeowners

Industry/Entity Type

Electrical Contractor

Requirements
Must have
• Monthly or Seasonal Themes

```html
<!DOCTYPE html>
<html lang="en">
<head>
<meta charset="utf-8">
<title>Clear Current Monthly – July 2024 Edition</title>
<link href="https://fonts.googleapis.com/css2?family=Archivo:ital,wght@0,400;0,500;0,600;0,700;1,400;1,600;1,700&display=swap" rel="stylesheet">
<style>
  :root {
    --navy: #12163a;
    --navy-deep: #0d1030;
    --ink: #161a3c;
    --white: #ffffff;
    --stage: #b3b3b3;
    --red: #d8202f;
    --blue: #2f55b5;
  }
  * { box-sizing: border-box; margin: 0; padding: 0; }
  html, body { width: 720px; height: 1200px; overflow: hidden; background: var(--stage); }
  body { font-family: "Archivo", Arial, sans-serif; color: var(--ink); position: relative; }

  .newsletter {
    position: absolute; left: 80px; top: 42px;
    width: 932px; height: 1860px;
    transform: scale(0.6); transform-origin: top left;
    background: var(--white);
    box-shadow: 0 14px 40px rgba(0,0,0,.35);
  }
  .block { position: absolute; }

  /* Header */
  .masthead { left: 0; top: 0; width: 932px; height: 490px; background: var(--navy); }
  .fireworks-top {
    position: absolute; left: 0; top: 0; width: 932px; height: 200px;
    background:
      radial-gradient(circle at 8% 15%, rgba(216,32,47,.55) 0 3%, transparent 14%),
      radial-gradient(circle at 20% 50%, rgba(47,85,181,.5) 0 3%, transparent 16%),
      radial-gradient(circle at 42% 20%, rgba(216,32,47,.45) 0 3%, transparent 15%),
      radial-gradient(circle at 62% 25%, rgba(47,85,181,.5) 0 3%, transparent 16%),
      radial-gradient(circle at 90% 45%, rgba(216,32,47,.6) 0 3%, transparent 15%),
      radial-gradient(circle at 78% 10%, rgba(255,255,255,.25) 0 2%, transparent 10%),
      linear-gradient(to bottom, var(--navy-deep), var(--navy));
  }
  .issue-name { left: 59px; top: 187px; color: var(--white); font-weight: 600; font-size: 14.5px; line-height: 23px; }
  .hero-title { left: 59px; top: 253px; color: var(--white); font-weight: 700; font-size: 36px; line-height: 45px; }
  .hero-greeting { left: 59px; top: 372px; color: var(--white); font-size: 14.5px; }
  .hero-intro { left: 59px; top: 408px; width: 802px; color: var(--white); font-size: 14.5px; line-height: 18.3px; text-align: justify; }

  /* Columns */
  .column { top: 527px; width: 371px; font-size: 14.5px; line-height: 18.2px; }
  .column-left { left: 59px; }
  .column-right { left: 493px; }
  .section-heading { font-size: 18.5px; line-height: 22px; font-weight: 400; color: var(--ink); }
  .section-heading strong { font-weight: 700; }
  .heading-rule { width: 86px; height: 3px; background: var(--ink); margin: 15px 0 22px; }
  .column p { margin-bottom: 18px; text-align: justify; }
  .column p.flush, .column p.signoff { text-align: left; }
  .spaced { margin-top: 30px; }

  .tip-list { list-style: none; margin-top: 0; }
  .tip { position: relative; height: 62px; margin-bottom: 5px; }
  .tip-box {
    position: absolute; left: 30px; top: 0; width: 337px; height: 62px;
    border: 1.6px solid var(--ink); border-radius: 9px;
    padding: 13px 8px 0 34px; font-size: 11px; line-height: 16px;
    color: var(--ink); background: var(--white); text-align: left;
  }
  .tip-box strong { font-weight: 700; }
  .tip-icon { position: absolute; left: 3px; top: 4px; width: 54px; height: 54px; z-index: 1; }
  .closing-note { font-style: italic; font-size: 14.5px; margin-top: 20px; }

  /* Ask an expert band */
  .expert-band { left: 0; top: 1201px; width: 932px; height: 353px; background: var(--navy); color: var(--white); }
  .fireworks-faint {
    position: absolute; left: 0; top: 0; width: 932px; height: 140px;
    background:
      radial-gradient(circle at 6% 30%, rgba(216,32,47,.18) 0 3%, transparent 14%),
      radial-gradient(circle at 30% 20%, rgba(47,85,181,.2) 0 3%, transparent 15%),
      radial-gradient(circle at 58% 15%, rgba(216,32,47,.16) 0 3%, transparent 15%),
      radial-gradient(circle at 84% 40%, rgba(216,32,47,.22) 0 3%, transparent 16%),
      radial-gradient(circle at 96% 20%, rgba(47,85,181,.2) 0 3%, transparent 12%),
      linear-gradient(to bottom, #161a44, var(--navy));
  }
  .expert-content { position: absolute; left: 59px; top: 51px; width: 820px; font-size: 14.5px; line-height: 18.2px; }
  .expert-content .section-heading { color: var(--white); }
  .expert-content .heading-rule { background: var(--white); margin: 15px 0 22px; }
  .stay-connected { display: flex; align-items: center; gap: 20px; margin: 20px 0 24px; }
  .stay-connected em { font-weight: 700; font-size: 18px; }
  .social-links { display: flex; gap: 8px; }
  .social-dot { width: 20px; height: 20px; border-radius: 50%; background: var(--white); }
  .expert-content p { margin-bottom: 18px; }

  /* Footer */
  .company-footer { left: 59px; top: 1588px; width: 820px; font-size: 14.5px; line-height: 18.2px; }
  .company-name { font-size: 18px; font-weight: 700; line-height: 20px; }
  .tagline { font-style: italic; margin-bottom: 18px; }
  .company-footer p { margin-bottom: 18px; text-align: justify; }
</style>
</head>
<body>
<main class="newsletter">

  <header class="block masthead">
    <div class="fireworks-top" role="img" aria-label="Independence Day fireworks bursts and star-spangled bunting in red, white and blue"></div>
    <div class="block issue-name">Clear Current Monthly<br>July 2024 Edition</div>
    <h1 class="block hero-title">Welcome to<br>Clear Current Monthly!</h1>
    <p class="block hero-greeting">Hello, valued clients and partners!</p>
    <p class="block hero-intro">We are thrilled to welcome you to the inaugural issue of our monthly newsletter, designed to keep you informed about the latest trends, tips, and updates in the electrical contracting world. Whether you're a homeowner, business owner, or industry professional, there's something here for everyone.</p>
  </header>

  <section class="block column column-left">
    <h2 class="section-heading"><strong>A Warm Welcome from Our CEO</strong></h2>
    <div class="heading-rule"></div>
    <p class="flush">Greetings!</p>
    <p>I'm delighted to introduce you to our new monthly newsletter, Clear Current Monthly. At Tolvan Wiring, we are committed to excellence, safety, and innovation in all our electrical projects. Through this newsletter, we aim to share our knowledge, celebrate our successes, and strengthen our relationship with you.</p>
    <p>I want to thank all of our clients for your business and your partnership. The journey has been amazing. We are thrilled to welcome you to the inaugural issue of our monthly newsletter, designed to keep you informed about the latest trends, tips, and updates in the electrical contracting world. Whether you're a homeowner, business owner, or industry professional, there's something here for everyone.</p>
    <p>I also wanted to introduce some new programs we are introducing. We are offering a Home Membership program [tolvanwiring], a referral program [tolvanwiring], and free VideoMeet estimates [tolvanwiring]. We have started a non-profit aimed at helping lower-income households with electrical work that is hazardous at a discounted price or at no cost, on a case-by-case basis. This is in the beginning stages, and we will keep you updated as this progresses. Our non-profit is called Brightway Home Aid. Stay tuned for more updates!</p>
    <p class="signoff">Sincerely,<br>Daniel Marsh<br>CEO, Tolvan Wiring LLC</p>
  </section>

  <section class="block column column-right">
    <h2 class="section-heading"><strong>Project Spotlight:</strong> Green Energy Initiative</h2>
    <div class="heading-rule"></div>
    <p>This month, we're excited to highlight our recent work on the Green Energy Initiative. Our team is currently replacing @ 400 fluorescent light fixtures with LEDs, significantly reducing this client's carbon footprint and energy costs. This project underscores our dedication to sustainable and environmentally friendly solutions.</p>

    <h2 class="section-heading spaced"><strong>Safety First:</strong> Summer Electrical Safety Tips</h2>
    <div class="heading-rule"></div>
    <p>As temperatures rise, so does the risk of electrical hazards. Here are some tips to keep your home and workplace safe this summer:</p>

    <ul class="tip-list">
      <li class="tip">
        <svg class="tip-icon" viewBox="0 0 54 54" aria-hidden="true">
          <circle cx="27" cy="27" r="26" fill="#fff" stroke="#161a3c" stroke-width="1.4" stroke-dasharray="2 2"/>
          <circle cx="27" cy="27" r="22" fill="#161a3c"/>
          <circle cx="27" cy="27" r="10" fill="none" stroke="#fff" stroke-width="2"/>
          <line x1="27" y1="27" x2="33" y2="21" stroke="#fff" stroke-width="2" stroke-linecap="round"/>
          <circle cx="27" cy="27" r="2" fill="#fff"/>
        </svg>
        <div class="tip-box"><strong>Avoid Overloading Circuits:</strong> Ensure that air conditioners and other heavy-duty appliances are on separate circuits.</div>
      </li>
      <li class="tip">
        <svg class="tip-icon" viewBox="0 0 54 54" aria-hidden="true">
          <circle cx="27" cy="27" r="26" fill="#fff" stroke="#161a3c" stroke-width="1.4" stroke-dasharray="2 2"/>
          <circle cx="27" cy="27" r="22" fill="#161a3c"/>
          <circle cx="30" cy="24" r="7" fill="none" stroke="#fff" stroke-width="2"/>
          <line x1="25" y1="29" x2="18" y2="36" stroke="#fff" stroke-width="2.4" stroke-linecap="round"/>
        </svg>
        <div class="tip-box"><strong>Inspect Electrical Cords:</strong> Replace any damaged or frayed cords immediately.</div>
      </li>
      <li class="tip">
        <svg class="tip-icon" viewBox="0 0 54 54" aria-hidden="true">
          <circle cx="27" cy="27" r="26" fill="#fff" stroke="#161a3c" stroke-width="1.4" stroke-dasharray="2 2"/>
          <circle cx="27" cy="27" r="22" fill="#161a3c"/>
          <path d="M24 15 C20 22 17 26 17 30 a7 7 0 0 0 14 0 C31 26 28 22 24 15Z" fill="none" stroke="#fff" stroke-width="1.8"/>
          <line x1="27" y1="32" x2="37" y2="32" stroke="#fff" stroke-width="1.8"/>
          <line x1="29" y1="36" x2="37" y2="36" stroke="#fff" stroke-width="1.8"/>
        </svg>
        <div class="tip-box"><strong>Stay Dry:</strong> Keep electrical devices away from water sources, especially pools and sprinklers.</div>
      </li>
      <li class="tip">
        <svg class="tip-icon" viewBox="0 0 54 54" aria-hidden="true">
          <circle cx="27" cy="27" r="26" fill="#fff" stroke="#161a3c" stroke-width="1.4" stroke-dasharray="2 2"/>
          <circle cx="27" cy="27" r="22" fill="#161a3c"/>
          <rect x="15" y="18" width="24" height="18" rx="2" fill="none" stroke="#fff" stroke-width="1.8"/>
          <rect x="19" y="22" width="6" height="10" fill="none" stroke="#fff" stroke-width="1.4"/>
          <rect x="29" y="22" width="6" height="10" fill="none" stroke="#fff" stroke-width="1.4"/>
        </svg>
        <div class="tip-box"><strong>Use GFCIs:</strong> Install Ground Fault Circuit Interrupters in areas prone to moisture to prevent shocks.</div>
      </li>
    </ul>
    <p class="closing-note">Stay safe and enjoy a worry-free summer!</p>
  </section>

  <section class="block expert-band">
    <div class="fireworks-faint" role="img" aria-label="Faint fireworks and flag bunting decoration"></div>
    <div class="expert-content">
      <h2 class="section-heading"><strong>Ask an Expert:</strong> Your Questions Answered</h2>
      <div class="heading-rule"></div>
      <p>Have questions about electrical systems, safety, or new technologies? Our experts are here to help! Send your questions to info@tolvanwiring.com and we'll feature the answers in our next newsletter.</p>
      <div class="stay-connected">
        <em>Stay Connected!</em>
        <div class="social-links" aria-label="Social media links">
          <span class="social-dot"></span><span class="social-dot"></span><span class="social-dot"></span>
        </div>
      </div>
      <p>Thank you for reading Clear Current Monthly. We look forward to bringing you more valuable insights and updates next month!</p>
      <p>Best regards,<br>The Team at Tolvan Wiring LLC<br>(555) 014-2287</p>
    </div>
  </section>

  <footer class="block company-footer">
    <div class="company-name">Tolvan Wiring LLC</div>
    <div class="tagline">Electrical Excellence. Unmatched Service.</div>
    <p>I want to thank all of our clients for your business and your partnership. The journey has been amazing. We are thrilled to welcome you to the inaugural issue of our monthly newsletter, designed to keep you informed about the latest trends, tips, and updates in the electrical contracting world. Whether you're a homeowner, business owner, or industry professional, there's something here for everyone.</p>
    <p>I also wanted to introduce some new programs we are introducing. We are offering a Home Membership program [tolvanwiring], a referral program [tolvanwiring], and free VideoMeet estimates [tolvanwiring]. We have started a non-profit aimed at helping lower-income households with electrical work that is hazardous at a discounted price or at no cost, on a case-by-case basis. This is in the beginning stages, and we will keep you updated as this progresses. Our non-profit is called Brightway Home Aid. Stay tuned for more updates!</p>
  </footer>

</main>
</body>
</html>
```